Flyer Redesign for Commerical Painting Company in South Australia

RM HOLLOWAY COATINGS — CAPABILITY FLYER SET REFRESH
We are RM Holloway Coatings Contractors, a family-owned painting business in Adelaide, South Australia, trading since 1982. We have five existing capability flyers — Strata, Heritage, Facilities Maintenance, Commercial, and Aged Care. We would like an additional 6th one done that is 'Designer/Architect' aimed. They work, but they look templated. We want them rebuilt as one premium, on-brand family: same look on every page, elevated execution, and zero design inconsistency between them.
IMPORTANT: This is a SET, not five separate jobs. The single most important outcome is that all five look like they were made by the same studio at the same time. Nail one master layout and flow all five flyers through it.
BRAND ASSETS
Our Style Guide plus logos are attached and is the source of truth. The colours, fonts, and logo usage in the guide override anything you see in the current flyers.
Quick orientation:
- Logo: "RM HOLLOWAY COATINGS" stacked mark with the multi-shape icon (red / blue / yellow), sitting above the strapline HERITAGE | COMMERCIAL | RESIDENTIAL. Always keep that strapline locked to the logo.
- Brand colours: blue (primary), red (signal), yellow (accent). Use the exact hex/CMYK values in the Style Guide.
- Tone: established, trusted, award-winning, family-owned.
If any asset (font file, vector logo, hex codes) is missing from the attachment, please ask before starting — do not substitute look-alikes.
WHAT TO KEEP
These elements already create cohesion — keep the concept, just raise the craft:
- The top credentials row of six icons (24-Hour Quote, Professional Project Management, 5-Year Workmanship Warranty, Experience, Guild Finishers Award, Quality Paints). Keep six markers; redraw the icons in one consistent premium style.
- A large hero image near the top of page 1.
- Three supporting columns of body copy.
- A "Featured Projects" page 2 with a clean image grid and captions.
- A footer band carrying the contact and tagline.
WHAT TO CHANGE
- Replace the light-blue / cyan title banner blocks. They look dated. Use a restrained premium header instead — brand navy, or clean white with a single thin accent rule. No bright cyan fill.
- Change centred body copy to left-aligned text on a strict grid. Left-alignment reads more professional.
- Add whitespace. Give the copy room to breathe. Premium means generous margins, not crammed text.
- Use one bespoke, consistent icon set. Standardise the label wording and length.
- Use one identical footer system across all five flyers.
- Make the hero imagery the visual anchor — larger, sharper, with the same framing treatment applied identically on every flyer.
- Establish a clear premium type hierarchy (display heading, section heading, body, caption) per the Style Guide and apply it identically across all five.
- The only thing that should differ between flyers is a single category accent (e.g. a category label or one tinted element) so each service is instantly readable. Structure, type, footer, and icon row stay identical.
COPY
Please use the copy that is currently in the documents. This may change for us in the future but it will suit for the time being.
For the 'Designer/Architect' flyer please use this copy:
RM Holloway Coatings Contractors is a proud South Australian family-owned business
that has been helping clients transform and maintain their properties for over 40
years.
Founded in 1982, we have built our reputation on quality workmanship, honest
communication, and lasting relationships. Whether it's a family home, apartment
complex, office space, retail environment, heritage building, or commercial interior,
we understand that paint plays an important role in creating spaces that people enjoy
living and working in.
Our team of fully employed, trade-qualified painters takes pride in delivering
exceptional finishes that not only enhance the appearance of a property but also
complement its character, atmosphere, and purpose. From refreshing residential
interiors to revitalising commercial environments and preserving heritage assets, we
work closely with our clients to achieve results that are both practical and visually
appealing.
Our services include:
ï‚· External Painting
ï‚· Internal Painting
ï‚· Wallpaper Installation & Removal
ï‚· French Wash Finishes
ï‚· Lime Wash Application
ï‚· Heritage Restoration, Conservation & Maintenance Works
ï‚· Low VOC & Leaf Mark Approved Coating Applications
ï‚· High Access Painting & Maintenance Works
As a family business, we believe in personal service, attention to detail, and treating
every project as if it were our own. This commitment has earned us the trust of
homeowners, businesses, and property managers across South Australia for more
than four decades.
At RM Holloway Coatings Contractors, we're passionate about creating spaces that look
beautiful, feel welcoming, and stand the test of time while protecting and preserving
the assets entrusted to our care.
FORMAT AND SPECS
- Size: A4 portrait (210 x 297 mm), 2 pages per flyer (front + Featured Projects).
- Bleed: 3 mm all edges, with crop marks on the print export.
- Colour: supply both a print-ready CMYK version (PDF/X) and a digital RGB version (these are emailed and viewed on screen as well as printed).
- Resolution: 300 dpi for all placed imagery.
DELIVERABLES
For each of the 6 flyers (both pages):
1. Print-ready PDF (CMYK, 3 mm bleed, crop marks).
2. Digital PDF (RGB, no bleed/marks, optimised for email).
3. PNG or JPG of each page (RGB, for web/social).
4. We would like an editable file so we can change the copy when required and images. We predominantly use Canva in these situations but are open to suggestion.
PLEASE AVOID
- Bright cyan / baby-blue banner fills. We would be okay using the #01385D colour.
- Centred body paragraphs.
- Stock-photo cliches (handshakes, ladders, generic team shots) — use the project imagery we supply or just have a boxed area where we can add imagery.
- More than three accent colours on a page.
- Drop shadows, bevels, or gradients that fight the clean brand look.
- Any deviation in layout, type, or footer between the five flyers.
HOW WE WILL LOOK AT SUBMISSIONS
1. Cohesion — do all five read as one family? (Most important.)
2. Premium feel — does it look like a high-end contractor, not a template?
3. Brand fidelity — does it match the attached Style Guide?
4. Usability — clean hierarchy, legible, print and screen ready.
RM Holloway Coatings Contractors — Heritage | Commercial | Residential. Trusted across South Australia since 1982.

```html
<!DOCTYPE html>
<html lang="en">
<head>
<meta charset="utf-8">
<title>RM Holloway Coatings – Designer / Architect Flyer</title>
<link href="https://fonts.googleapis.com/css2?family=Montserrat:wght@400;500;600;700;800&display=swap" rel="stylesheet">
<style>
  :root{
    --navy:#14214b;
    --navy-deep:#101b3f;
    --red:#d9272e;
    --ink:#2b3048;
    --muted:#5a5f72;
    --cream:#f7f3ea;
    --rule:#d9dbe3;
    --page:#ffffff;
    --backdrop:#c9cbcf;
  }
  *{box-sizing:border-box;margin:0;padding:0}
  html,body{width:1200px;height:2270px;overflow:hidden}
  body{background:var(--backdrop);font-family:'Montserrat',sans-serif;color:var(--ink)}
  .sheet{position:absolute;left:205px;width:790px;height:1117px;background:var(--page);overflow:hidden}
  .sheet--front{top:12px}
  .sheet--projects{top:1141px}

  /* header */
  .brand{position:absolute;left:40px;top:40px;display:flex;align-items:center;gap:12px}
  .brand__mark{width:40px;height:40px;background:var(--red)}
  .brand__name{font-weight:800;color:var(--navy);font-size:22px;line-height:1.05;letter-spacing:.5px}
  .category{position:absolute;right:40px;top:52px;font-size:14px;font-weight:600;color:var(--navy);letter-spacing:.4px;padding-bottom:8px;border-bottom:2px solid var(--red)}

  /* hero */
  .hero{position:absolute;left:0;top:138px;width:772px;height:360px;background:linear-gradient(160deg,#eef0ef 0%,#dcdcd6 40%,#9e9587 70%,#6a6258 100%)}
  .hero__title{position:absolute;left:40px;top:388px;font-size:37px;font-weight:700;line-height:1.03;color:var(--navy);letter-spacing:-.5px}
  .hero__title::after{content:"";display:block;width:40px;height:3px;background:var(--red);margin-top:12px}

  /* credentials */
  .credentials{position:absolute;left:40px;top:516px;width:712px;height:110px;display:flex}
  .credential{flex:1;display:flex;flex-direction:column;align-items:center;text-align:center;border-left:1px solid var(--rule);padding-top:4px}
  .credential:first-child{border-left:none}
  .credential svg{width:46px;height:46px;stroke:var(--navy);fill:none;stroke-width:2;stroke-linecap:round;stroke-linejoin:round}
  .credential__label{margin-top:8px;font-size:11px;font-weight:600;line-height:1.3;color:var(--navy)}

  /* body columns */
  .column{position:absolute;top:652px}
  .column h2,.services h2{font-size:15px;font-weight:600;color:var(--navy)}
  .column h2::after,.services h2::after{content:"";display:block;width:24px;height:2px;background:var(--red);margin:8px 0 14px}
  .column p{font-size:8.4px;line-height:1.65;color:var(--ink);margin-bottom:15px}
  .column--about{left:40px;width:152px}
  .column--approach{left:214px;width:158px}
  .column--commitment{left:397px;width:162px}
  .services{position:absolute;left:575px;top:634px;width:178px;height:348px;background:var(--cream);border:1px solid #ece6d8;padding:16px 14px}
  .services ul{list-style:none}
  .services li{position:relative;padding-left:18px;font-size:8.6px;font-weight:600;line-height:1.35;color:var(--navy);margin-bottom:11px}
  .services li svg{position:absolute;left:0;top:0;width:11px;height:11px}

  /* footer */
  .footer{position:absolute;left:0;bottom:0;width:100%;height:98px;background:var(--navy-deep);display:flex;align-items:center;padding:0 40px;color:#fff}
  .footer__item{display:flex;align-items:center;gap:10px;font-size:10px;font-weight:500}
  .footer__item svg{width:22px;height:22px;stroke:#fff;fill:none;stroke-width:1.6;stroke-linecap:round;stroke-linejoin:round}
  .footer__divider{width:2px;height:30px;background:var(--red);margin:0 24px}
  .footer__tagline{margin-left:auto;text-align:center;font-size:11px;font-weight:500;line-height:1.3}
  .footer__tagline::after{content:"";display:block;width:26px;height:2px;background:var(--red);margin:6px auto 0}

  /* projects page */
  .projects__title{position:absolute;left:40px;top:150px;font-size:23px;font-weight:700;color:var(--navy);letter-spacing:.3px}
  .projects__title::after{content:"";display:block;width:46px;height:3px;background:var(--red);margin-top:8px}
  .projects__intro{position:absolute;left:40px;top:212px;width:590px;font-size:10px;line-height:1.5;color:var(--ink)}
  .project{position:absolute;width:232px}
  .project__image{height:238px}
  .project h3{margin-top:14px;font-size:11px;font-weight:700;color:var(--navy)}
  .project__place{font-size:9.5px;color:var(--muted);margin-top:3px}
  .project__note{font-size:9.5px;line-height:1.45;color:var(--muted);margin-top:8px;width:210px}
</style>
</head>
<body>

<!-- Page 1 -->
<section class="sheet sheet--front">
  <div class="brand"><span class="brand__mark"></span><span class="brand__name">RM HOLLOWAY<br>COATINGS</span></div>
  <div class="category">DESIGNER / ARCHITECT</div>

  <div class="hero" role="img" aria-label="Photograph of a bright architectural interior with a white spiral staircase, tall glazing, a cream sofa and timber arched doorway"></div>
  <h1 class="hero__title">Finishes that<br>inspire spaces.</h1>

  <div class="credentials">
    <div class="credential">
      <svg viewBox="0 0 48 48"><circle cx="28" cy="26" r="14"/><path d="M28 18v8l5 4M25 9h6M28 9v3M6 20h8M4 26h9M6 32h8"/></svg>
      <span class="credential__label">24-Hour<br>Quote</span>
    </div>
    <div class="credential">
      <svg viewBox="0 0 48 48"><circle cx="24" cy="14" r="5"/><circle cx="12" cy="20" r="4"/><circle cx="36" cy="20" r="4"/><path d="M15 36c0-6 4-10 9-10s9 4 9 10zM4 36c0-5 3-8 8-8M44 36c0-5-3-8-8-8"/></svg>
      <span class="credential__label">Professional<br>Project<br>Management</span>
    </div>
    <div class="credential">
      <svg viewBox="0 0 48 48"><path d="M24 5l15 6v11c0 10-7 17-15 21C16 39 9 32 9 22V11z"/><path d="M17 24l5 5 9-10"/></svg>
      <span class="credential__label">5-Year<br>Workmanship<br>Warranty</span>
    </div>
    <div class="credential">
      <svg viewBox="0 0 48 48"><path d="M12 10c-6 8-6 20 4 28M36 10c6 8 6 20-4 28"/><text x="24" y="28" text-anchor="middle" font-size="11" font-weight="700" font-family="Montserrat,sans-serif" fill="#14214b" stroke="none">40+</text></svg>
      <span class="credential__label">40+ Years<br>Experience</span>
    </div>
    <div class="credential">
      <svg viewBox="0 0 48 48"><path d="M15 7h18v10c0 6-4 10-9 10s-9-4-9-10zM15 11H8c0 6 3 9 7 9M33 11h7c0 6-3 9-7 9M24 27v8M16 41h16l-2-6H18z"/></svg>
      <span class="credential__label">Guild<br>Finishers<br>Award</span>
    </div>
    <div class="credential">
      <svg viewBox="0 0 48 48"><ellipse cx="24" cy="12" rx="13" ry="4"/><path d="M11 12v24c0 2 6 4 13 4s13-2 13-4V12M11 20c0 2 6 4 13 4s13-2 13-4"/></svg>
      <span class="credential__label">Quality<br>Paint<br>Systems</span>
    </div>
  </div>

  <div class="column column--about">
    <h2>About Us</h2>
    <p>RM Holloway Coatings Contractors is a proud South Australian family-owned business that has been helping clients transform and maintain their properties for over 40 years.</p>
    <p>Founded in 1982, we have built our reputation on quality workmanship, honest communication, and lasting relationships.</p>
    <p>As a family business, we believe in personal service, attention to detail, and treating every project as if it were our own.</p>
  </div>

  <div class="column column--approach">
    <h2>Our Approach</h2>
    <p>Whether it's a family home, apartment complex, office space, retail environment, heritage building, or commercial interior, we understand that paint plays an important role in creating spaces that people enjoy living and working in.</p>
    <p>Our team of fully employed, trade-qualified painters takes pride in delivering exceptional finishes that not only enhance the appearance of a property but also complement its character, atmosphere, and purpose.</p>
    <p>We work closely with our clients to achieve results that are both practical and visually appealing.</p>
  </div>

  <div class="column column--commitment">
    <h2>Our Commitment</h2>
    <p>From refreshing residential interiors to revitalising commercial environments and preserving heritage assets, we bring experience, care, and craftsmanship to every project.</p>
    <p>This commitment has earned us the trust of homeowners, businesses, and property managers across South Australia for more than four decades.</p>
    <p>At RM Holloway Coatings Contractors, we're passionate about creating spaces that look beautiful, feel welcoming, and stand the test of time while protecting and preserving the assets entrusted to our care.</p>
  </div>

  <aside class="services">
    <h2>Our Services</h2>
    <ul>
      <li><svg viewBox="0 0 12 12"><circle cx="6" cy="6" r="6" fill="#14214b"/><path d="M3.3 6.2l1.8 1.8 3.6-3.6" stroke="#fff" stroke-width="1.3" fill="none"/></svg>External Painting</li>
      <li><svg viewBox="0 0 12 12"><circle cx="6" cy="6" r="6" fill="#14214b"/><path d="M3.3 6.2l1.8 1.8 3.6-3.6" stroke="#fff" stroke-width="1.3" fill="none"/></svg>Internal Painting</li>
      <li><svg viewBox="0 0 12 12"><circle cx="6" cy="6" r="6" fill="#14214b"/><path d="M3.3 6.2l1.8 1.8 3.6-3.6" stroke="#fff" stroke-width="1.3" fill="none"/></svg>Wallpaper Installation<br>&amp; Removal</li>
      <li><svg viewBox="0 0 12 12"><circle cx="6" cy="6" r="6" fill="#14214b"/><path d="M3.3 6.2l1.8 1.8 3.6-3.6" stroke="#fff" stroke-width="1.3" fill="none"/></svg>French Wash Finishes</li>
      <li><svg viewBox="0 0 12 12"><circle cx="6" cy="6" r="6" fill="#14214b"/><path d="M3.3 6.2l1.8 1.8 3.6-3.6" stroke="#fff" stroke-width="1.3" fill="none"/></svg>Lime Wash Application</li>
      <li><svg viewBox="0 0 12 12"><circle cx="6" cy="6" r="6" fill="#14214b"/><path d="M3.3 6.2l1.8 1.8 3.6-3.6" stroke="#fff" stroke-width="1.3" fill="none"/></svg>Heritage Restoration,<br>Conservation &amp; Maintenance<br>Works</li>
      <li><svg viewBox="0 0 12 12"><circle cx="6" cy="6" r="6" fill="#14214b"/><path d="M3.3 6.2l1.8 1.8 3.6-3.6" stroke="#fff" stroke-width="1.3" fill="none"/></svg>Low VOC &amp; Leaf Mark<br>Approved Coating<br>Applications</li>
      <li><svg viewBox="0 0 12 12"><circle cx="6" cy="6" r="6" fill="#14214b"/><path d="M3.3 6.2l1.8 1.8 3.6-3.6" stroke="#fff" stroke-width="1.3" fill="none"/></svg>High Access Painting &amp;<br>Maintenance Works</li>
    </ul>
  </aside>

  <footer class="footer">
    <div class="footer__item"><svg viewBox="0 0 24 24"><path d="M5 3h4l2 5-2.5 1.5a11 11 0 0 0 6 6L16 13l5 2v4a2 2 0 0 1-2 2A17 17 0 0 1 3 5a2 2 0 0 1 2-2z"/></svg>(08) 8000 4127</div>
    <span class="footer__divider"></span>
    <div class="footer__item"><svg viewBox="0 0 24 24"><rect x="3" y="5" width="18" height="14" rx="1"/><path d="M3 6l9 7 9-7"/></svg>office@rmhollowaycoatings.com.au</div>
    <span class="footer__divider"></span>
    <div class="footer__item"><svg viewBox="0 0 24 24"><circle cx="12" cy="12" r="9"/><path d="M3 12h18M12 3c3 3 3 15 0 18M12 3c-3 3-3 15 0 18"/></svg>rmhollowaycoatings.com.au</div>
    <span class="footer__divider"></span>
    <div class="footer__tagline">Serving South Australia<br>Since 1982</div>
  </footer>
</section>

<!-- Page 2 -->
<section class="sheet sheet--projects">
  <div class="brand"><span class="brand__mark"></span><span class="brand__name">RM HOLLOWAY<br>COATINGS</span></div>
  <div class="category">DESIGNER / ARCHITECT</div>

  <h1 class="projects__title">FEATURED PROJECTS</h1>
  <p class="projects__intro">We partner with designers and architects to deliver exceptional finishes that enhance the vision, character and functionality of every space. Here is a selection of projects that reflect our craftsmanship, attention to detail and commitment to quality.</p>

  <article class="project" style="left:40px;top:282px">
    <div class="project__image" role="img" aria-label="Photograph of a sandstone heritage facade with arched windows" style="background:linear-gradient(170deg,#8fa06a 0%,#c9a57c 35%,#b88a5e 100%)"></div>
    <h3>Heritage Restoration</h3>
    <div class="project__place">North Adelaide, SA</div>
    <p class="project__note">Restoration and repainting of heritage facade and architectural detailing.</p>
  </article>
  <article class="project" style="left:280px;top:282px">
    <div class="project__image" role="img" aria-label="Photograph of a bright commercial office reception with curved ceiling" style="background:linear-gradient(170deg,#f1f0ec 0%,#e4e0d8 55%,#c9bda8 100%)"></div>
    <h3>Commercial Interior</h3>
    <div class="project__place">Adelaide CBD, SA</div>
    <p class="project__note">High-end interior repainting with premium finishes to office fit-out.</p>
  </article>
  <article class="project" style="left:522px;top:282px">
    <div class="project__image" role="img" aria-label="Photograph of a modern white apartment building with glass balconies under blue sky" style="background:linear-gradient(170deg,#6f9fd6 0%,#dfe3e6 45%,#8f9298 100%)"></div>
    <h3>Residential Apartments</h3>
    <div class="project__place">Glenelg, SA</div>
    <p class="project__note">External painting of modern apartment complex with durable, long-lasting systems.</p>
  </article>

  <article class="project" style="left:40px;top:646px">
    <div class="project__image" role="img" aria-label="Photograph of a boutique retail interior with arched wall niches and clothing rails" style="background:linear-gradient(170deg,#f0e9df 0%,#ddd1bf 50%,#a99580 100%)"></div>
    <h3>Retail Environment</h3>
    <div class="project__place">Norwood, SA</div>
    <p class="project__note">Full interior repaint and feature wall finishes for boutique retail store.</p>
  </article>
  <article class="project" style="left:280px;top:646px">
    <div class="project__image" role="img" aria-label="Photograph of a stone heritage church with a tall spire under blue sky" style="background:linear-gradient(170deg,#3f78c8 0%,#8aa8d0 35%,#a38a6a 75%,#6f5b44 100%)"></div>
    <h3>Heritage Conservation</h3>
    <div class="project__place">Adelaide Hills, SA</div>
    <p class="project__note">Conservation and protective coating application to heritage building.</p>
  </article>
  <article class="project" style="left:522px;top:646px">
    <div class="project__image" role="img" aria-label="Photograph of a modern education building walkway with a timber-lined canopy" style="background:linear-gradient(170deg,#2f3338 0%,#d79a45 30%,#e6e4de 60%,#9fb3c8 100%)"></div>
    <h3>Education Facility</h3>
    <div class="project__place">Mount Barker, SA</div>
    <p class="project__note">Internal and external painting to new education facility.</p>
  </article>

  <footer class="footer">
    <div class="footer__item"><svg viewBox="0 0 24 24"><path d="M5 3h4l2 5-2.5 1.5a11 11 0 0 0 6 6L16 13l5 2v4a2 2 0 0 1-2 2A17 17 0 0 1 3 5a2 2 0 0 1 2-2z"/></svg>(08) 8000 4127</div>
    <span class="footer__divider"></span>
    <div class="footer__item"><svg viewBox="0 0 24 24"><rect x="3" y="5" width="18" height="14" rx="1"/><path d="M3 6l9 7 9-7"/></svg>office@rmhollowaycoatings.com.au</div>
    <span class="footer__divider"></span>
    <div class="footer__item"><svg viewBox="0 0 24 24"><circle cx="12" cy="12" r="9"/><path d="M3 12h18M12 3c3 3 3 15 0 18M12 3c-3 3-3 15 0 18"/></svg>rmhollowaycoatings.com.au</div>
    <span class="footer__divider"></span>
    <div class="footer__tagline">Serving South Australia<br>Since 1982</div>
  </footer>
</section>

</body>
</html>
```